Need App for Impact Related Events

My app is to help with internal events. When you enter the prompted event code the next screen shows you everyone currently at the event. It will give you the ability to Start a conversation with someone you met at that event, or signal it is your turn to send a message. The next screen is a message thread with that person. I am looking for a design that incorporates the colors and ‘feel good’ emotion of our logo. I have pieced together a pretty good interpretation of what I’m looking for in the attached mockup by slicing and dicing designs. I also attached our logo mascot.Screens (see attached mockups)

Note 1: I do not like the picture on the screen used in screen one because it makes it seem like a dating app. I attached an alternative photo that can be used or present different ideas.

Note 2: On the login/signup screen (screen 2) I need an additional first and last name for login, you can try to fit this on one login screen or present a two step signup screen where that is presented in the second screen.

READ MOCKUP GUIDELINES UNDER Must Haves

Target Market(s)

People attending internal social impact events

Industry/Entity Type

Charity

Font styles to use
Sans Serif

Colors
86cfc6

Requirements
Must have
• Follow the screen mockups attached to project
• PLEASE READ
• I have provided a relatively close design of what I’m looking for in the mockups. Some screens need to be followed more closely to my design mockup than other. I have listed a guide below how how closely you should follow my mockup design exactly. Overall I would like to see some ideas of incorporating a few accent colors so it doesn’t appear SO Blue. I also attached some app inspiration designs I found from around the web
• Screen Mockup Guideline Follow %
• Screen 1: 65% - mostly on target, would like to see ways to make it not SO Blue and possibly creative places to add some explainer text describing the app
• Screen 2: 50% - general design idea is here, but more open
• Screen 3: 35% - a lot more room for design influence
• Screen 4: 70% - mostly on target, a little room for design influence/color scheme ideas
• Screen 5-6: 25% - a lot of room for design change/ideas/influence
• Screen 7-8: 80% - already very close to what I need, maybe open to slight sizing and color scheme ideas
• Screen 9: 15% - the most open for influence, only the general functionality of the screen is communicated here
Nice to have
• Please Read Mockup Guideline above. In large part I am looking for something to use some nice accent colors so it is not overwhelmingly blue and bring the whole design into a seamless style.
Should not have

```html
<!DOCTYPE html>
<html lang="en">
<head>
<meta charset="utf-8">
<title>KindHive – Login screens</title>
<link rel="stylesheet" href="https://fonts.googleapis.com/css2?family=Inter:wght@400;500;600&display=swap">
<style>
  :root {
    --page-bg: #ffffff;
    --screen-bg: #ffffff;
    --screen-edge: #e4e8ea;
    --ink: #1c2430;
    --ink-soft: #5b6470;
    --muted: #7d8590;
    --rule: #d9dee2;
    --mint-wash: #dff8f5;
    --mint-wash-light: #f0fcfa;
    --mint-btn: #2ff2d8;
    --mint-btn-edge: #1fcfb8;
    --sky-btn: #40bbff;
    --sky-btn-edge: #2a9fe0;
    --navy-btn: #244f8b;
    --white: #ffffff;
    --logo-ink: #16181b;
  }
  * { box-sizing: border-box; margin: 0; padding: 0; }
  html, body {
    width: 1200px; height: 1200px; overflow: hidden;
    background: var(--page-bg);
    font-family: "Inter", Arial, sans-serif;
    color: var(--ink);
  }
  .canvas { position: relative; width: 1200px; height: 1200px; }

  .screen {
    position: absolute; top: 180px;
    width: 390px; height: 840px;
    background: var(--screen-bg);
    border-radius: 36px;
    overflow: hidden;
    box-shadow: 0 0 0 1px var(--screen-edge), 0 12px 30px rgba(20, 40, 60, .08);
  }
  .screen--mint { left: 140px; }
  .screen--sky { left: 671px; }

  .status-bar {
    position: absolute; top: 18px; left: 0; width: 100%; height: 24px;
    padding: 0 26px 0 36px;
    display: flex; justify-content: space-between; align-items: center;
    font-size: 14px; font-weight: 600;
  }
  .status-icons { display: flex; gap: 6px; align-items: center; }

  .nav-bar {
    position: absolute; top: 52px; left: 0; width: 100%; height: 40px;
    border-bottom: 1px solid var(--rule);
    display: flex; align-items: center; justify-content: center;
    font-size: 16px; font-weight: 400;
  }
  .nav-back { position: absolute; left: 16px; top: 10px; }

  .hero-wash { position: absolute; top: 93px; left: 0; width: 100%; height: 460px; }

  .brand { position: absolute; top: 108px; left: 0; width: 100%; text-align: center; }
  .brand-mark {
    width: 86px; height: 86px; margin: 0 auto;
    border-radius: 50%; background: var(--white);
    box-shadow: 0 6px 14px rgba(40, 120, 110, .12);
  }
  .brand-name {
    margin-top: 22px;
    font-size: 32px; font-weight: 500; letter-spacing: -.5px;
    color: var(--logo-ink);
  }

  .field {
    position: absolute; left: 30px; width: 326px;
    border-bottom: 1px solid var(--rule);
    padding-bottom: 12px;
    font-size: 17px; color: var(--ink-soft);
  }
  .field--email { top: 296px; }
  .field--password { top: 372px; }

  .pill {
    position: absolute; left: 70px; width: 250px; height: 54px;
    border-radius: 27px;
    display: flex; align-items: center; justify-content: center; gap: 10px;
    color: var(--white); font-size: 17px; font-weight: 500; letter-spacing: .3px;
  }
  .login-btn { top: 448px; }
  .login-btn--mint { background: var(--mint-btn); box-shadow: 0 3px 0 var(--mint-btn-edge); }
  .login-btn--sky { background: var(--sky-btn); box-shadow: 0 3px 0 var(--sky-btn-edge); }
  .social-btn { top: 603px; height: 52px; background: var(--navy-btn); font-weight: 600; }
  .social-dot { width: 10px; height: 10px; border-radius: 50%; background: var(--white); }

  .divider {
    position: absolute; top: 542px; left: 0; width: 100%;
    display: flex; align-items: center; gap: 22px;
    font-size: 14px; color: var(--ink);
  }
  .divider::before, .divider::after { content: ""; flex: 1; height: 1px; background: var(--rule); }

  .signup { position: absolute; top: 758px; left: 0; width: 100%; text-align: center; }
  .signup-hint { font-size: 14px; color: var(--muted); }
  .signup-link { margin-top: 4px; font-size: 25px; font-weight: 500; color: var(--ink); }
</style>
</head>
<body>
<main class="canvas">

  <section class="screen screen--mint" aria-label="Login screen, mint variant">
    <svg class="hero-wash" viewBox="0 0 390 460" preserveAspectRatio="none" aria-hidden="true">
      <defs>
        <linearGradient id="wash-mint" x1="0" y1="0" x2="0" y2="1">
          <stop offset="0" stop-color="#dff8f5"/>
          <stop offset=".8" stop-color="#e9faf8"/>
          <stop offset="1" stop-color="#ffffff" stop-opacity="0"/>
        </linearGradient>
      </defs>
      <rect width="390" height="460" fill="url(#wash-mint)"/>
      <path d="M0 0 H390 V75 C320 95 250 70 170 30 C110 5 50 12 0 20 Z" fill="#f0fcfa"/>
    </svg>
    <div class="status-bar">
      <span>9:41</span>
      <span class="status-icons">
        <svg width="18" height="13" viewBox="0 0 18 13" aria-hidden="true"><path d="M9 12 L6.5 9.2 A3.6 3.6 0 0 1 11.5 9.2 Z M3.8 6.6 A7.4 7.4 0 0 1 14.2 6.6 L12.8 8 A5.4 5.4 0 0 0 5.2 8 Z M1 3.8 A11.4 11.4 0 0 1 17 3.8 L15.6 5.2 A9.4 9.4 0 0 0 2.4 5.2 Z" fill="#1c2430"/></svg>
        <svg width="26" height="12" viewBox="0 0 26 12" aria-hidden="true"><rect x=".5" y=".5" width="22" height="11" rx="3" fill="none" stroke="#1c2430"/><rect x="2" y="2" width="19" height="8" rx="1.5" fill="#1c2430"/><rect x="23.5" y="4" width="1.6" height="4" rx=".8" fill="#1c2430"/></svg>
      </span>
    </div>
    <header class="nav-bar">
      <svg class="nav-back" width="14" height="22" viewBox="0 0 14 22" aria-hidden="true"><path d="M11 2 L3 11 L11 20" fill="none" stroke="#1c2430" stroke-width="2.2" stroke-linecap="round" stroke-linejoin="round"/></svg>
      <span>Login</span>
    </header>
    <div class="brand">
      <div class="brand-mark"></div>
      <div class="brand-name">KindHive</div>
    </div>
    <div class="field field--email">Email ID</div>
    <div class="field field--password">Password (6+ characters)</div>
    <div class="pill login-btn login-btn--mint">LOGIN</div>
    <div class="divider">Or, Login with</div>
    <div class="pill social-btn"><span class="social-dot"></span>LINKUP</div>
    <div class="signup">
      <p class="signup-hint">Don’t have Account?</p>
      <p class="signup-link">Sign Up</p>
    </div>
  </section>

  <section class="screen screen--sky" aria-label="Login screen, sky variant">
    <svg class="hero-wash" viewBox="0 0 390 460" preserveAspectRatio="none" aria-hidden="true">
      <defs>
        <linearGradient id="wash-sky" x1="0" y1="0" x2="0" y2="1">
          <stop offset="0" stop-color="#dff8f5"/>
          <stop offset=".8" stop-color="#e9faf8"/>
          <stop offset="1" stop-color="#ffffff" stop-opacity="0"/>
        </linearGradient>
      </defs>
      <rect width="390" height="460" fill="url(#wash-sky)"/>
      <path d="M0 0 H390 V75 C320 95 250 70 170 30 C110 5 50 12 0 20 Z" fill="#f0fcfa"/>
    </svg>
    <div class="status-bar">
      <span>9:41</span>
      <span class="status-icons">
        <svg width="18" height="13" viewBox="0 0 18 13" aria-hidden="true"><path d="M9 12 L6.5 9.2 A3.6 3.6 0 0 1 11.5 9.2 Z M3.8 6.6 A7.4 7.4 0 0 1 14.2 6.6 L12.8 8 A5.4 5.4 0 0 0 5.2 8 Z M1 3.8 A11.4 11.4 0 0 1 17 3.8 L15.6 5.2 A9.4 9.4 0 0 0 2.4 5.2 Z" fill="#1c2430"/></svg>
        <svg width="26" height="12" viewBox="0 0 26 12" aria-hidden="true"><rect x=".5" y=".5" width="22" height="11" rx="3" fill="none" stroke="#1c2430"/><rect x="2" y="2" width="19" height="8" rx="1.5" fill="#1c2430"/><rect x="23.5" y="4" width="1.6" height="4" rx=".8" fill="#1c2430"/></svg>
      </span>
    </div>
    <header class="nav-bar">
      <svg class="nav-back" width="14" height="22" viewBox="0 0 14 22" aria-hidden="true"><path d="M11 2 L3 11 L11 20" fill="none" stroke="#1c2430" stroke-width="2.2" stroke-linecap="round" stroke-linejoin="round"/></svg>
      <span>Login</span>
    </header>
    <div class="brand">
      <div class="brand-mark"></div>
      <div class="brand-name">KindHive</div>
    </div>
    <div class="field field--email">Email ID</div>
    <div class="field field--password">Password (6+ characters)</div>
    <div class="pill login-btn login-btn--sky">LOGIN</div>
    <div class="divider">Or, Login with</div>
    <div class="pill social-btn"><span class="social-dot"></span>LINKUP</div>
    <div class="signup">
      <p class="signup-hint">Don’t have Account?</p>
      <p class="signup-link">Sign Up</p>
    </div>
  </section>

</main>
</body>
</html>
```